Fahrzeugbeschriftung für mittelständische Abbruch- und Schadstoffsanierungsfirma
Zielgruppe
Wir sind eine mittelständische Abbruch- und Schadstoffsanierungsfirma.
Aufgabenstellung
Unsere Fahrzeuge haben bereits Werbung, jedoch soll das Design für ein Halvorn Trekka überarbeitet und modernisiert werden. Jedoch soll der Stil ähnlich bleiben.

```html
<!DOCTYPE html>
<html lang="de">
<head>
<meta charset="utf-8">
<title>Brevik Haus und Bauservice – Fahrzeugbeschriftung Halvorn Trekka</title>
<link rel="stylesheet" href="https://fonts.googleapis.com/css2?family=Roboto:wght@400;500;700&display=swap">
<style>
  :root {
    --brand-red: #e3141b;
    --pill-black: #1d1d1b;
    --panel-white: #ffffff;
    --canvas-bg: #f2f2f2;
    --panel-edge: #d6d6d6;
    --text-dark: #1d1d1b;
  }
  * { box-sizing: border-box; margin: 0; padding: 0; }
  html, body { width: 1200px; height: 794px; overflow: hidden; background: var(--canvas-bg); }
  body { font-family: "Roboto", Arial, sans-serif; }

  .wrap-side {
    position: absolute; left: 40px; top: 130px; width: 1120px; height: 480px;
    background: var(--panel-white); border: 2px solid var(--panel-edge); border-radius: 28px;
    overflow: hidden;
  }
  .wrap-side__red { position: absolute; inset: 0; width: 100%; height: 100%; }

  .brand {
    position: absolute; left: 450px; top: 70px; width: 270px; text-align: center;
  }
  .brand__name {
    font-size: 50px; font-weight: 700; color: var(--text-dark); letter-spacing: 1px; line-height: 1;
    display: flex; align-items: center; justify-content: center; gap: 12px;
  }
  .brand__mark { width: 18px; height: 18px; background: var(--brand-red); }
  .brand__line {
    margin-top: 14px; font-size: 22px; font-weight: 500; color: var(--brand-red); letter-spacing: .5px;
  }
  .brand__tagline {
    margin-top: 4px; font-size: 9.5px; font-weight: 500; color: var(--text-dark); letter-spacing: .4px;
  }

  .web-address {
    position: absolute; left: 475px; top: 262px;
    font-size: 25px; font-weight: 500; color: var(--brand-red);
  }

  .services { position: absolute; left: 750px; top: 32px; list-style: none; }
  .services__item {
    display: block; margin-bottom: 7px; padding: 3px 20px 4px;
    background: var(--pill-black); color: #fff; border: 2px solid #fff; border-radius: 10px;
    font-size: 22px; font-weight: 500; line-height: 1.2; width: max-content;
  }
  .services__item:nth-child(2) { margin-left: 14px; }
  .services__item:nth-child(3) { margin-left: 28px; }
  .services__item:nth-child(4) { margin-left: 42px; }
  .services__item:nth-child(5) { margin-left: 56px; }

  .contact { position: absolute; left: 800px; top: 292px; list-style: none; }
  .contact__item {
    display: block; margin-bottom: 10px; padding: 3px 16px;
    background: var(--brand-red); color: #fff; border: 2px solid #fff; border-radius: 8px;
    font-size: 18px; font-weight: 400; line-height: 1.2; width: max-content;
  }
</style>
</head>
<body>
  <section class="wrap-side" aria-label="Seitenbeschriftung Halvorn Trekka">
    <svg class="wrap-side__red" viewBox="0 0 1120 480" preserveAspectRatio="none" aria-hidden="true">
      <polygon points="700,0 1120,0 1120,480 900,480 860,420 760,160" fill="var(--brand-red)"/>
    </svg>

    <div class="brand">
      <div class="brand__name"><span class="brand__mark"></span>BREVIK</div>
      <div class="brand__line">HAUS UND BAUSERVICE</div>
      <div class="brand__tagline">SCHADSTOFFSANIERUNG | ABBRUCH | ENTSORGUNG</div>
    </div>

    <p class="web-address">www.brevik-bau.de</p>

    <ul class="services">
      <li class="services__item">Industrierückbau</li>
      <li class="services__item">Abbruch &amp; Entkernen</li>
      <li class="services__item">Entsorgung</li>
      <li class="services__item">Schadstoffsanierung</li>
      <li class="services__item">Asbest, KMF, PAK</li>
    </ul>

    <ul class="contact">
      <li class="contact__item">0160 5812903</li>
      <li class="contact__item">anfrage@brevik-bau.de</li>
    </ul>
  </section>
</body>
</html>
```